Design Business Card - Redesign Truck Wrap

I have a business card design, but do not like it (see attached). Attached is my logo, i want to keep that the same, just change the business card layout and design. Keep the same information.

I also want to get ideas for a wrap for my truck (picture attached) using the same logo.

```html
<!DOCTYPE html>
<html lang="en">
<head>
<meta charset="utf-8">
<title>RKT Land Services – Business Card</title>
<link href="https://fonts.googleapis.com/css2?family=Poppins:wght@400;500;600;700&display=swap" rel="stylesheet">
<style>
  :root {
    --bg: #3a3a3a;
    --card: #f4f2ec;
    --orange: #e8702a;
    --grey: #6e6f73;
    --grey-light: #8a8b8f;
  }
  * { box-sizing: border-box; margin: 0; padding: 0; }
  html, body { width: 1200px; height: 900px; overflow: hidden; }
  body {
    background: radial-gradient(circle at 50% 45%, #4a4a4a, var(--bg) 70%);
    font-family: "Poppins", sans-serif;
    position: relative;
  }
  .card {
    position: absolute;
    top: 295px;
    width: 540px;
    height: 310px;
    background: var(--card);
    border-radius: 16px;
    overflow: hidden;
    box-shadow: 0 14px 30px rgba(0,0,0,.45);
  }
  .card--back { left: 30px; }
  .card--front { left: 630px; }

  /* shared wordmark */
  .wordmark { display: flex; align-items: center; gap: 10px; }
  .wordmark__dot { width: 14px; height: 14px; border-radius: 50%; background: var(--grey); }
  .wordmark__name { color: var(--orange); font-weight: 700; line-height: 1; }

  /* back side */
  .card--back .wordmark { position: absolute; top: 26px; left: 0; right: 0; justify-content: center; }
  .card--back .wordmark__name { font-size: 24px; letter-spacing: .5px; }
  .columns {
    position: absolute; top: 78px; left: 30px; right: 30px; bottom: 28px;
    display: grid; grid-template-columns: 1fr 2px 1fr; column-gap: 22px;
  }
  .divider { background: var(--orange); }
  .band {
    display: inline-block; background: var(--grey); color: var(--orange);
    font-size: 12px; font-weight: 600; letter-spacing: .6px; padding: 4px 10px; margin-bottom: 12px;
  }
  .contact { list-style: none; }
  .contact li { display: flex; align-items: flex-start; gap: 8px; margin-bottom: 8px; }
  .contact svg { flex: none; margin-top: 2px; }
  .contact__name { display: block; color: var(--orange); font-size: 13px; font-weight: 600; line-height: 1.2; }
  .contact__detail { display: block; color: var(--orange); font-size: 11.5px; line-height: 1.3; }
  .services { list-style: none; }
  .services li {
    display: flex; align-items: center; gap: 10px; color: var(--orange);
    font-size: 12px; font-weight: 500; letter-spacing: .3px; margin-bottom: 12px;
  }
  .services li::before {
    content: ""; width: 8px; height: 8px; border-radius: 50%; background: var(--orange); flex: none;
  }

  /* front side */
  .card--front .wordmark { position: absolute; top: 26px; left: 150px; }
  .card--front .wordmark__dot { width: 18px; height: 18px; }
  .front-title { display: flex; flex-direction: column; }
  .card--front .wordmark__name { font-size: 46px; letter-spacing: 1px; }
  .front-title__sub { color: var(--grey); font-size: 11px; letter-spacing: 4px; font-weight: 500; margin-top: 2px; }
  .truck-photo {
    position: absolute; right: 0; bottom: 0; width: 340px; height: 200px;
    background: linear-gradient(160deg, #e9e9e6 0%, #cfcfcb 45%, #8d8b86 75%, #3d3d3f 100%);
    border-top-left-radius: 10px;
  }
</style>
</head>
<body>

  <section class="card card--back" aria-label="Card back">
    <div class="wordmark">
      <span class="wordmark__dot"></span>
      <span class="wordmark__name">RKT LAND SERVICES</span>
    </div>
    <div class="columns">
      <div class="col col--contact">
        <span class="band">OWNER CONTACTS</span>
        <ul class="contact">
          <li>
            <svg width="12" height="12" viewBox="0 0 24 24" fill="#e8702a"><path d="M6.6 10.8a15 15 0 0 0 6.6 6.6l2.2-2.2a1 1 0 0 1 1-.25 11.4 11.4 0 0 0 3.6.6 1 1 0 0 1 1 1V20a1 1 0 0 1-1 1A17 17 0 0 1 3 4a1 1 0 0 1 1-1h3.5a1 1 0 0 1 1 1c0 1.25.2 2.45.6 3.6a1 1 0 0 1-.25 1z"/></svg>
            <span><span class="contact__name">MATEO RIVERA</span><span class="contact__detail">555.214.3380</span></span>
          </li>
          <li>
            <svg width="12" height="12" viewBox="0 0 24 24" fill="#e8702a"><path d="M6.6 10.8a15 15 0 0 0 6.6 6.6l2.2-2.2a1 1 0 0 1 1-.25 11.4 11.4 0 0 0 3.6.6 1 1 0 0 1 1 1V20a1 1 0 0 1-1 1A17 17 0 0 1 3 4a1 1 0 0 1 1-1h3.5a1 1 0 0 1 1 1c0 1.25.2 2.45.6 3.6a1 1 0 0 1-.25 1z"/></svg>
            <span><span class="contact__name">LUCAS D. RIVERA</span><span class="contact__detail">555.214.7715</span></span>
          </li>
          <li>
            <svg width="12" height="12" viewBox="0 0 24 24" fill="none" stroke="#6e6f73" stroke-width="2"><rect x="3" y="5" width="18" height="14" rx="1"/><path d="M3 6l9 7 9-7"/></svg>
            <span class="contact__detail">rktlandservices@mail.com</span>
          </li>
          <li>
            <svg width="12" height="12" viewBox="0 0 24 24" fill="none" stroke="#6e6f73" stroke-width="2"><circle cx="12" cy="12" r="9"/><path d="M3 12h18M12 3a14 14 0 0 1 0 18M12 3a14 14 0 0 0 0 18"/></svg>
            <span class="contact__detail">rktlandservices.com</span>
          </li>
        </ul>
      </div>
      <div class="divider"></div>
      <div class="col col--services">
        <span class="band">LICENSED &amp; INSURED</span>
        <ul class="services">
          <li>DUMPSTER RENTAL</li>
          <li>LAND CLEARING</li>
          <li>STONE AND SOIL</li>
          <li>SITE GRADING</li>
          <li>FORESTRY MULCHING</li>
        </ul>
      </div>
    </div>
  </section>

  <section class="card card--front" aria-label="Card front">
    <div class="wordmark">
      <span class="wordmark__dot"></span>
      <div class="front-title">
        <span class="wordmark__name">RKT</span>
        <span class="front-title__sub">LAND SERVICES</span>
      </div>
    </div>
    <div class="truck-photo" role="img" aria-label="Photo of the company's white work truck cab"></div>
  </section>

</body>
</html>
```